Basic business card

use my newly created logo - and the phrases (Lower Cost of Test & Accelarated New Product Introduction) - and my new email domain / ID - use at conferences / tradeshows

Industry/Entity Type

semiconductor

Contact Information for Business Card

Lewis K Hardy, Owner, communicate via Logo - Lower COT - Cost of Test, Accelerated NPI - New Product Introduction, phone +1 480 555 0162, Chandler, Arizona, USA, lewis.hardy@vexalon-tsq.com

Font styles to use
Sans Serif

Requirements
Nice to have
• re-use my logo created via Artisan Hive last August (#5918206)

```html
<!DOCTYPE html>
<html lang="en">
<head>
<meta charset="utf-8">
<title>VEXALON Business Card</title>
<link href="https://fonts.googleapis.com/css2?family=Montserrat:wght@400;500;600;700&display=swap" rel="stylesheet">
<style>
  :root {
    --stage: #e9e6e1;
    --card-white: #ffffff;
    --card-slate: #4b5772;
    --ink: #4a5570;
    --ink-soft: #6a6f7a;
    --text: #3d4250;
    --rule: #5b6275;
    --orange: #e9a03a;
    --sky: #4bbbe2;
    --green: #7ab72e;
    --blue: #1c6fb0;
    --emboss: #8f9ab2;
  }
  * { box-sizing: border-box; margin: 0; padding: 0; }
  html, body {
    width: 900px; height: 1200px; overflow: hidden;
    background: var(--stage);
    font-family: "Montserrat", sans-serif;
  }
  .canvas { position: relative; width: 900px; height: 1200px; }
  .card {
    position: absolute; left: 80px; width: 742px; height: 442px;
    border-radius: 30px; overflow: hidden;
    box-shadow: 0 4px 10px rgba(0,0,0,0.25);
  }
  .card--front { top: 130px; background: var(--card-white); }
  .card--back { top: 638px; background: var(--card-slate); }
  .color-band {
    position: absolute; left: 0; right: 0; bottom: 0; height: 14px; display: flex;
  }
  .color-band span { flex: 1; }
  .color-band .orange { background: var(--orange); }
  .color-band .sky { background: var(--sky); }
  .color-band .green { background: var(--green); }
  .color-band .blue { background: var(--blue); }

  .brand { position: absolute; display: flex; align-items: center; }
  .brand__mark { display: block; }
  .brand__name { font-weight: 600; letter-spacing: 1px; line-height: 1; }
  .card--front .brand { left: 46px; top: 212px; gap: 12px; }
  .card--front .brand__mark { width: 30px; height: 30px; background: var(--sky); }
  .card--front .brand__name { font-size: 42px; color: var(--ink); }
  .card--back .brand { left: 105px; top: 182px; gap: 18px; }
  .card--back .brand__mark { width: 62px; height: 62px; background: var(--emboss); }
  .card--back .brand__name { font-size: 84px; color: var(--emboss); }

  .divider {
    position: absolute; left: 395px; top: 132px; width: 2px; height: 188px;
    background: var(--rule);
  }
  .contact { position: absolute; left: 430px; top: 130px; color: var(--text); }
  .contact__name { font-size: 25px; font-weight: 700; color: var(--ink); line-height: 1.1; }
  .contact__role { font-size: 16px; color: var(--ink-soft); margin-top: 2px; }
  .contact__list { list-style: none; margin-top: 18px; }
  .contact__list li {
    display: flex; align-items: center; gap: 16px;
    font-size: 15.5px; height: 22.5px;
  }
  .contact__list svg { width: 14px; height: 14px; flex: none; }
  .contact__address { font-size: 16.5px; line-height: 20px; margin-top: 18px; }
</style>
</head>
<body>
<div class="canvas">
  <section class="card card--front">
    <div class="brand">
      <span class="brand__mark"></span>
      <span class="brand__name">VEXALON</span>
    </div>
    <div class="divider"></div>
    <div class="contact">
      <div class="contact__name">Lewis Hardy</div>
      <div class="contact__role">Owner</div>
      <ul class="contact__list">
        <li>
          <svg viewBox="0 0 14 14" aria-hidden="true"><path fill="#e9a03a" d="M2 4c0-2 2-3 5-3s5 1 5 3v1H9V4H5v1H2zM3 6h8l1 6H2z"/><circle cx="7" cy="9" r="1.5" fill="#fff"/></svg>
          <span>+1 480 555 0162</span>
        </li>
        <li>
          <svg viewBox="0 0 14 14" aria-hidden="true"><rect x="1" y="3" width="12" height="8" fill="#4bbbe2"/><path d="M1 3l6 5 6-5" fill="none" stroke="#fff" stroke-width="1"/></svg>
          <span>lewis.hardy@vexalon-tsq.com</span>
        </li>
        <li>
          <svg viewBox="0 0 14 14" aria-hidden="true"><circle cx="7" cy="7" r="6" fill="#1c6fb0"/><path d="M4 4c2 1 2 3 1 4s1 3 2 3M9 3c-1 2 1 3 2 3" fill="none" stroke="#fff" stroke-width="1"/></svg>
          <span>www.vexalon-tsq.com</span>
        </li>
      </ul>
      <div class="contact__address">418 West Harbor Rd, #112<br>Chandler, AZ 85225</div>
    </div>
    <div class="color-band"><span class="orange"></span><span class="sky"></span><span class="green"></span><span class="blue"></span></div>
  </section>

  <section class="card card--back">
    <div class="brand">
      <span class="brand__mark"></span>
      <span class="brand__name">VEXALON</span>
    </div>
    <div class="color-band"><span class="orange"></span><span class="sky"></span><span class="green"></span><span class="blue"></span></div>
  </section>
</div>
</body>
</html>
```